Emergency Vehicle Installer and Security Firm Needs a Business Card

Our company "Corvalt" need a business card for our Emergency Vehicle Equipment Installation and Infrastructure Security Business. We are contract designers, manufacturers and installers for Emergency Vehicle Fleets. This includes installation of Emergency Lights, Sirens, Vehicle Graphics and Radio Communications. We also supply this products to an international market. We also do consultant, and installation of high level security access, alarm and surveillance equipment for medium to large size businesses.

The design should represent a level of trust in our professionalism and expertise. It should visually display our ongoing relationship with the emergency services, but not overtake our commitment to high level security options.

Target Market(s)

Emergency Services and Businesses requiring high level security

Industry/Entity Type

Business

Contact Information for Business Card

*note complete details will be given to the winning designer for revising. The name "Mark Pell will be used to fill in name".

Mark Pell
Managing Director
Corvalt NZ Limited
Phone: +64 027 604 91352
Email: mark.pell@corvalt-example.co.nz

Requirements
Must have
• Card must be in black. Using our logo on the top as supplied. Designers should try having the reverse side as a blurred image of police lights (red and blue) with our logo in greyscale in the centre (this is not particularly a requirement, but feel free to play around with this option).
Nice to have
• A card design that looks good when spot UV printed. A clean compact and graphic design. A grey scale feel on the front (excluding logo, but you can play around with that idea). Rounded smooth text.
Should not have
• Will update this section as designs come through - feel free to submit what you feel would look good.

```html
<!DOCTYPE html>
<html lang="en">
<head>
<meta charset="utf-8">
<title>Corvalt Business Card</title>
<link rel="stylesheet" href="https://fonts.googleapis.com/css2?family=Open+Sans:wght@400;600;800&display=swap">
<style>
  :root {
    --page: #2b2b2b;
    --card: #0d0d0d;
    --card-back: #1a1a1a;
    --red: #e31e24;
    --white: #ffffff;
    --rule: #6a6a6a;
    --mark-faint: #3a3a3a;
  }
  * { margin: 0; padding: 0; box-sizing: border-box; }
  html, body {
    width: 1200px; height: 1189px; overflow: hidden;
    background: var(--page);
    font-family: "Open Sans", Arial, sans-serif;
  }
  .card {
    position: absolute; left: 170px; width: 860px; height: 492px;
    border-radius: 28px; overflow: hidden;
  }
  .card-back { top: 60px; background: var(--card-back); }
  .card-front { top: 637px; background: var(--card); }

  .back-name {
    position: absolute; left: 0; right: 0; top: 190px;
    text-align: center; font-weight: 800; font-size: 104px;
    letter-spacing: 2px; color: var(--mark-faint);
  }

  .front-name {
    position: absolute; left: 70px; top: 78px;
    font-weight: 800; font-size: 100px; letter-spacing: 1px;
    color: var(--white); line-height: 1;
  }
  .divider {
    position: absolute; left: 100px; top: 272px; width: 520px; height: 1px;
    background: var(--rule);
  }
  .person { position: absolute; left: 640px; top: 220px; }
  .person-name { font-weight: 800; font-size: 30px; color: var(--red); line-height: 1.1; }
  .person-title { font-weight: 400; font-size: 22px; color: var(--white); }

  .contacts { position: absolute; left: 110px; top: 370px; list-style: none; }
  .contacts li {
    display: flex; align-items: center; gap: 14px;
    font-size: 24px; color: var(--white); line-height: 1.45;
  }
  .contacts svg { width: 24px; height: 24px; flex: none; }

  .website {
    position: absolute; right: 60px; top: 370px;
    font-size: 22px; color: var(--white);
  }
  .band-white {
    position: absolute; left: 0; bottom: 0; width: 560px; height: 20px;
    background: var(--white);
  }
  .band-red {
    position: absolute; left: 575px; right: 0; bottom: 0; height: 60px;
    background: var(--red);
  }
</style>
</head>
<body>
  <section class="card card-back" aria-label="Card reverse">
    <div class="back-name">CORVALT</div>
  </section>

  <section class="card card-front" aria-label="Card front">
    <div class="front-name">CORVALT</div>
    <div class="divider"></div>
    <div class="person">
      <div class="person-name">Mark Pell</div>
      <div class="person-title">Managing Director</div>
    </div>
    <ul class="contacts">
      <li>
        <svg viewBox="0 0 24 24" aria-hidden="true">
          <rect width="24" height="24" rx="4" fill="#e31e24"/>
          <path d="M6 9c0-2 2-3 6-3s6 1 6 3v1h-3V9H9v1H6z M7 12h10l1 6H6z" fill="#0d0d0d"/>
        </svg>
        +64 027 604 91352
      </li>
      <li>
        <svg viewBox="0 0 24 24" aria-hidden="true">
          <rect width="24" height="24" rx="4" fill="#e31e24"/>
          <rect x="5" y="7" width="14" height="10" fill="none" stroke="#0d0d0d" stroke-width="1.6"/>
          <path d="M5 7l7 6 7-6M5 17l5-5M19 17l-5-5" fill="none" stroke="#0d0d0d" stroke-width="1.6"/>
        </svg>
        mark.pell@corvalt-example.co.nz
      </li>
    </ul>
    <div class="website">www.corvalt-example.co.nz</div>
    <div class="band-white"></div>
    <div class="band-red"></div>
  </section>
</body>
</html>
```